New SKINCARE Label Design Project

Check out our website www.morlenbloom.com. We offer a few products that are all natural, from drinks to skincare. We have new packaging for the "Dewhaven Balm" and need a new label design. We'd like out of the box thinking, but it should fit the existing concept. The product label should contain cool words, can be creative and should contain ingredients as this is a regulation.

I have added some examples of what we’d like. Please base your design on this.

Target Market(s)

skincare, cosmetics, natural, cool, young

Industry/Entity Type

Skin Care Product

Requirements
Must have
• Label must fit the existing concept, but should be out of the box, potentially using unexpected colors... Clean design, clean fonts, very professional, but playful at the same time, can maybe include cartoons, stars,...
Nice to have
• Out of the box thinking, we'd like to stand out from all other brands by label design, it should catch the eye and interest people to buy our product.

```html
<!DOCTYPE html>
<html lang="nl">
<head>
<meta charset="utf-8">
<title>Dewhaven Balm – Label</title>
<link href="https://fonts.googleapis.com/css2?family=Montserrat:wght@400;500&family=Lato:wght@300&family=Arimo:wght@400;700&family=Oswald:wght@600&display=swap" rel="stylesheet">
<style>
  :root {
    --page-bg: #eef2f6;
    --mint-top: #a9e6c9;
    --mint-bottom: #d3f2e3;
    --ink: #1f1f1f;
    --ink-soft: #3a3f3c;
    --band: #5d5d5d;
    --band-text: #ffffff;
    --wash-light: #e9efec;
    --wash-mid: #c9d6d0;
    --wash-deep: #aebfb7;
    --title-box: #f4f5f4;
    --title-border: #bfc3c1;
    --spark: #ffffff;
    --spark-accent: #f3c64d;
  }
  html, body {
    margin: 0;
    width: 908px;
    height: 1200px;
    overflow: hidden;
    background: var(--page-bg);
  }
  .canvas {
    position: relative;
    width: 908px;
    height: 1200px;
  }
  .label {
    position: absolute;
    left: 134px;
    top: 60px;
    width: 640px;
    height: 1080px;
    overflow: hidden;
    box-shadow: 0 6px 24px rgba(60, 80, 90, 0.12);
  }
  .label__mint {
    position: absolute;
    inset: 0 0 auto 0;
    height: 700px;
    background: linear-gradient(180deg, var(--mint-top), var(--mint-bottom));
  }
  .label__sprigs {
    position: absolute;
    inset: 0;
    width: 640px;
    height: 700px;
  }
  .sparkles {
    position: absolute;
    inset: 0;
    width: 640px;
    height: 700px;
  }
  .sparkle { fill: var(--spark); }
  .sparkle--accent { fill: var(--spark-accent); }
  .brand {
    position: absolute;
    top: 70px;
    width: 100%;
    text-align: center;
    color: var(--ink);
    font-family: "Montserrat", sans-serif;
  }
  .brand__name {
    font-size: 104px;
    font-weight: 400;
    line-height: 1;
    letter-spacing: 1px;
  }
  .brand__tagline {
    margin-top: 14px;
    font-size: 17px;
    font-weight: 500;
    letter-spacing: 2.5px;
  }
  .product-title {
    position: absolute;
    left: 170px;
    top: 410px;
    width: 300px;
    height: 136px;
    box-sizing: border-box;
    background: var(--title-box);
    border: 3px solid var(--title-border);
    box-shadow: 0 3px 10px rgba(0, 0, 0, 0.15);
    display: flex;
    align-items: center;
    justify-content: center;
    text-align: center;
    font-family: "Lato", sans-serif;
    font-weight: 300;
    font-size: 38px;
    line-height: 1.15;
    letter-spacing: 1px;
    color: var(--ink);
    text-transform: uppercase;
  }
  .claim-band {
    position: absolute;
    top: 700px;
    left: 0;
    width: 100%;
    height: 50px;
    background: var(--band);
    color: var(--band-text);
    font-family: "Arimo", sans-serif;
    font-weight: 700;
    font-size: 14px;
    letter-spacing: 1.5px;
    line-height: 18px;
    padding: 7px 0 0 22px;
    box-sizing: border-box;
  }
  .label__wash {
    position: absolute;
    top: 750px;
    left: 0;
    width: 100%;
    height: 330px;
    background:
      radial-gradient(ellipse at 65% 55%, var(--wash-deep), transparent 60%),
      radial-gradient(ellipse at 20% 80%, var(--wash-mid), transparent 55%),
      linear-gradient(180deg, var(--wash-light), var(--wash-mid));
  }
  .benefits {
    position: absolute;
    top: 770px;
    left: 0;
    width: 100%;
    text-align: center;
    font-family: "Arimo", sans-serif;
    font-weight: 700;
    font-size: 14px;
    letter-spacing: 1.5px;
    line-height: 18px;
    color: var(--ink);
  }
  .ingredients {
    position: absolute;
    top: 846px;
    left: 22px;
    width: 596px;
    font-family: "Arimo", sans-serif;
    font-weight: 400;
    font-size: 11px;
    line-height: 15px;
    letter-spacing: 0.3px;
    color: var(--ink-soft);
  }
  .ingredients__label {
    font-weight: 700;
    text-transform: uppercase;
    letter-spacing: 1px;
  }
  .net-weight {
    position: absolute;
    top: 935px;
    left: 22px;
    display: flex;
    align-items: baseline;
    gap: 18px;
    color: var(--ink);
  }
  .net-weight__mark {
    font-family: "Montserrat", sans-serif;
    font-size: 44px;
    line-height: 1;
  }
  .net-weight__amount {
    font-family: "Oswald", sans-serif;
    font-weight: 600;
    font-size: 28px;
  }
</style>
</head>
<body>
<div class="canvas">
  <div class="label">
    <div class="label__mint">
      <svg class="label__sprigs" role="img" aria-label="Scattered dark botanical sprig illustrations on mint" viewBox="0 0 640 700"></svg>
      <svg class="sparkles" viewBox="0 0 640 700" aria-hidden="true">
        <path class="sparkle" d="M80 300 L85 315 L100 320 L85 325 L80 340 L75 325 L60 320 L75 315 Z"/>
        <path class="sparkle--accent" d="M560 330 L564 342 L576 346 L564 350 L560 362 L556 350 L544 346 L556 342 Z"/>
        <path class="sparkle" d="M520 600 L525 614 L539 619 L525 624 L520 638 L515 624 L501 619 L515 614 Z"/>
        <path class="sparkle--accent" d="M110 610 L113 619 L122 622 L113 625 L110 634 L107 625 L98 622 L107 619 Z"/>
        <path class="sparkle" d="M590 150 L593 159 L602 162 L593 165 L590 174 L587 165 L578 162 L587 159 Z"/>
        <path class="sparkle--accent" d="M50 180 L53 189 L62 192 L53 195 L50 204 L47 195 L38 192 L47 189 Z"/>
        <circle class="sparkle" cx="150" cy="440" r="4"/>
        <circle class="sparkle" cx="500" cy="470" r="5"/>
        <circle class="sparkle--accent" cx="320" cy="640" r="4"/>
      </svg>
    </div>

    <div class="brand">
      <div class="brand__name">Morlen</div>
      <div class="brand__tagline">THE BLOOM COMPANY</div>
    </div>

    <div class="product-title">Dewhaven<br>Balm</div>

    <div class="claim-band">Een hoogwaardig<br>huidverzorgingsproduct</div>

    <div class="label__wash" role="img" aria-label="Soft grey-green watercolour texture"></div>

    <div class="benefits">
      Voedt en beschermt de huid<br>
      Ruwe huid wordt zacht en glad<br>
      Vertraagt de veroudering van de huid
    </div>

    <p class="ingredients" style="margin:0">
      <span class="ingredients__label">Ingrediënten:</span>
      Aqua, Butyrospermum Parkii Butter, Glycerin, Cetearyl Alcohol, Aloe Barbadensis Leaf Juice,
      Simmondsia Chinensis Seed Oil, Calendula Officinalis Flower Extract, Tocopherol, Xanthan Gum, Parfum.
    </p>

    <div class="net-weight">
      <span class="net-weight__mark">℮</span>
      <span class="net-weight__amount">3,5oz / 100gr</span>
    </div>
  </div>
</div>
</body>
</html>
```